Homecare and Senior Living in the RENOVATION SECTION

Looking for an ad size 6.425 inches wide by 5 inches tall
Ad is for Pellard Homecare: It will be in the Kestrel Gazette on Sunday in the special section called Home renovations
Having the ad with maybe some images of home safety type things for elderly clients like ramps and grab bars but having images with caregivers assisting someone using those things.
Homecare should always be one word
Pellard homecare logo should not have the quote under it
Ad should have services offered
-Homemaker & Companion Aides
-Home Health Aides
-Skilled Nursing (RN/LPN)
-Bathing & Meal Service
-Medication Management
-Respite Services
Ad should say services available 24/7
The ad needs to have a look and feel for the renovation section. Maybe have something about safety with a caregiver, bathroom bars and caregiver helping someone walk with holding on to a rail in their home?
This would be something nice for the ad!
Transform your home with Expert care services!

None of these ads are anything we are looking for, I want to cancel all together.

Target Market(s)

Men and Women in Hawaii ages 45-105 years old looking for caregivers for themselves or aging parents

Industry/Entity Type

Homecare

Font styles to use
Sans Serif

Colors
0054AA
0677BA
7BADD7
CADEEF
E8F1F8
FFF300
FFF600
FEFA6F
FFFEC7
FFFEE8
EB3D1F
EC4F4E
F09395
F8D3D4
FCEDEE

Requirements
Must have
• Include our Website www.PellardCare.example Phone# (808) 555-0173 say CALL today for FREE consultation
Nice to have
• Look at our website to get a feel for the brand
Should not have
• no QR CODE

```html
<!DOCTYPE html>
<html lang="en">
<head>
<meta charset="utf-8">
<title>Pellard Homecare – Home Renovations Ad</title>
<link href="https://fonts.googleapis.com/css2?family=Source+Sans+3:wght@400;600;700&display=swap" rel="stylesheet">
<style>
  :root{
    --page:#e6e6e6;
    --paper:#ffffff;
    --blush:#f09395;
    --blush-light:#f8d3d4;
    --blush-pale:#fcedee;
    --navy:#0054aa;
    --blue:#0677ba;
    --sky:#7badd7;
    --ice:#e8f1f8;
    --coral:#ec4f4e;
    --check:#0677ba;
  }
  *{margin:0;padding:0;box-sizing:border-box}
  html,body{width:1200px;height:1200px;overflow:hidden;background:var(--page)}
  body{font-family:"Source Sans 3",Arial,sans-serif;position:relative}
  .ad{position:absolute;left:38px;top:90px;width:1123px;height:873px;background:var(--paper);overflow:hidden}

  .hero{position:absolute;left:0;top:0;width:1123px;height:374px;background:var(--blush)}
  .hero-photo{position:absolute;right:0;top:0;width:440px;height:366px;
    background:linear-gradient(90deg,rgba(240,147,149,1) 0%,rgba(240,147,149,0) 18%),
               linear-gradient(180deg,#d9d7d3 0%,#c2c0bc 55%,#7badd7 100%)}
  .hero-swoosh{position:absolute;left:0;top:196px;width:760px;height:40px}

  .headline-top{position:absolute;left:45px;top:34px;color:#fff;font-weight:700;line-height:1;white-space:nowrap}
  .headline-top .big{font-size:70px;letter-spacing:-0.5px}
  .headline-top .small{font-size:40px}
  .headline-band{position:absolute;left:0;top:112px;width:800px;height:84px;background:var(--navy);
    clip-path:polygon(0 0,100% 0,96% 100%,0 100%)}
  .headline-band span{position:absolute;left:45px;top:8px;color:#fff;font-weight:700;font-size:64px;line-height:1.1;white-space:nowrap;letter-spacing:-0.5px}

  .availability{position:absolute;left:45px;top:218px;display:flex;align-items:center;color:#fff}
  .availability svg{width:76px;height:80px}
  .availability .hours{margin-left:24px;font-size:100px;font-weight:700;line-height:1}
  .availability .label{margin-left:16px;font-size:36px;font-weight:600;line-height:1.15}

  .services-tab{position:absolute;left:0;top:321px;width:1123px;height:53px}
  .services-title{position:absolute;left:45px;top:327px;color:#fff;font-size:31px;font-weight:700;line-height:1.3}

  .service-list{position:absolute;left:45px;top:395px;list-style:none}
  .service-list li{display:flex;align-items:center;height:53.4px;font-size:30px;color:var(--navy);white-space:nowrap}
  .service-list svg{width:20px;height:20px;margin-right:10px;flex:none}

  .reno-title{position:absolute;left:622px;width:400px;top:386px;text-align:center;color:var(--navy);font-size:34px;font-weight:700}
  .photo{position:absolute;border-radius:24px}
  .photo-bath{left:556px;top:442px;width:278px;height:215px;background:linear-gradient(160deg,#f1e2b8,#e8e4dc 45%,#c38c57 100%)}
  .photo-fit{left:846px;top:442px;width:214px;height:112px;background:linear-gradient(120deg,#b9b0a4,#3a5a8c 55%,#c9dbe8)}
  .photo-assist{left:846px;top:563px;width:214px;height:94px;background:linear-gradient(90deg,#e9e4dc,#b98a62 45%,#3f6fc4 100%)}

  .footer-band{position:absolute;left:0;top:675px;width:1123px;height:198px}
  .cta{position:absolute;left:45px;top:742px;color:var(--navy);font-size:40px;font-weight:700;line-height:1.12}
  .contact{position:absolute;left:437px;top:738px;width:430px}
  .contact .row{display:flex;align-items:center;white-space:nowrap}
  .contact .phone{font-size:50px;font-weight:600;color:var(--coral);line-height:1.1}
  .contact .web{font-size:33px;font-weight:700;color:var(--navy);line-height:1.3;margin-top:4px}
  .contact svg{width:22px;height:22px;margin-right:10px;flex:none}

  .brand{position:absolute;left:905px;top:683px;width:180px;text-align:center}
  .brand .mark{width:60px;height:60px;margin:0 auto 12px;background:var(--blush);border-radius:8px}
  .brand .name{font-size:36px;font-weight:700;color:var(--navy);line-height:1.05}
</style>
</head>
<body>
<main class="ad">
  <section class="hero">
    <div class="hero-photo" role="img" aria-label="Smiling senior woman in a floral gown seated on a shower chair holding bathroom grab bars"></div>
    <svg class="hero-swoosh" viewBox="0 0 760 40" preserveAspectRatio="none"><path d="M0 0 L760 0 Q400 30 0 10 Z" fill="var(--blush-light)" opacity="0.35"/></svg>

    <h1 class="headline-top"><span class="big">Transform</span> <span class="small">your home with</span></h1>
    <div class="headline-band"><span>Expert care services!</span></div>

    <div class="availability">
      <svg viewBox="0 0 76 80" fill="none" stroke="#fff" stroke-width="2.6" stroke-linecap="round" stroke-linejoin="round">
        <path d="M14 30 A26 26 0 0 1 60 16"/>
        <path d="M56 10 L61 17 L53 19"/>
        <path d="M66 34 A26 26 0 0 1 54 54"/>
        <circle cx="38" cy="26" r="7"/>
        <path d="M26 46 Q38 32 50 46 Z"/>
        <path d="M4 58 L18 52 Q26 50 34 54 L44 54 Q48 56 44 60 L32 60"/>
        <path d="M44 58 L62 50 Q68 50 64 56 L44 70 Q36 74 26 70 L14 68"/>
        <path d="M2 56 L10 76"/>
      </svg>
      <span class="hours">24/7</span>
      <span class="label">Services<br>Available</span>
    </div>

    <svg class="services-tab" viewBox="0 0 1123 53" preserveAspectRatio="none">
      <path d="M0 0 L350 0 Q380 0 410 20 Q450 45 490 45 L1123 45 L1123 53 L0 53 Z" fill="var(--navy)"/>
    </svg>
    <h2 class="services-title">Services Offered:</h2>
  </section>

  <ul class="service-list">
    <li><svg viewBox="0 0 20 20" fill="none" stroke="var(--check)" stroke-width="1.6" stroke-linecap="round"><path d="M16 7 A8 8 0 1 1 12 3"/><path d="M6 10 L9 13 L18 3"/></svg>Homemaker &amp; Companion Aides</li>
    <li><svg viewBox="0 0 20 20" fill="none" stroke="var(--check)" stroke-width="1.6" stroke-linecap="round"><path d="M16 7 A8 8 0 1 1 12 3"/><path d="M6 10 L9 13 L18 3"/></svg>Home Health Aides</li>
    <li><svg viewBox="0 0 20 20" fill="none" stroke="var(--check)" stroke-width="1.6" stroke-linecap="round"><path d="M16 7 A8 8 0 1 1 12 3"/><path d="M6 10 L9 13 L18 3"/></svg>Skilled Nursing (RN/LPN)</li>
    <li><svg viewBox="0 0 20 20" fill="none" stroke="var(--check)" stroke-width="1.6" stroke-linecap="round"><path d="M16 7 A8 8 0 1 1 12 3"/><path d="M6 10 L9 13 L18 3"/></svg>Bathing &amp; Meal Service</li>
    <li><svg viewBox="0 0 20 20" fill="none" stroke="var(--check)" stroke-width="1.6" stroke-linecap="round"><path d="M16 7 A8 8 0 1 1 12 3"/><path d="M6 10 L9 13 L18 3"/></svg>Medication Management</li>
    <li><svg viewBox="0 0 20 20" fill="none" stroke="var(--check)" stroke-width="1.6" stroke-linecap="round"><path d="M16 7 A8 8 0 1 1 12 3"/><path d="M6 10 L9 13 L18 3"/></svg>Respite Services</li>
  </ul>

  <h2 class="reno-title">Home Renovations</h2>
  <div class="photo photo-bath" role="img" aria-label="Accessible bathroom with grab bars, shower rail and vanity"></div>
  <div class="photo photo-fit" role="img" aria-label="Technician installing a grab bar while a homeowner watches"></div>
  <div class="photo photo-assist" role="img" aria-label="Caregiver in scrubs holding the hands of a senior walking"></div>

  <svg class="footer-band" viewBox="0 0 1123 198" preserveAspectRatio="none">
    <defs>
      <linearGradient id="footerFade" x1="0" x2="1" y1="0" y2="0">
        <stop offset="0" stop-color="#e2e2e2"/>
        <stop offset="0.6" stop-color="#f7f7f7"/>
        <stop offset="1" stop-color="#ffffff"/>
      </linearGradient>
    </defs>
    <path d="M0 48 L390 48 Q415 48 440 32 Q480 5 520 5 L1123 5 L1123 198 L0 198 Z" fill="url(#footerFade)"/>
  </svg>

  <p class="cta">CALL today for<br>FREE consultation</p>

  <div class="contact">
    <div class="row phone">
      <svg viewBox="0 0 24 24" fill="none" stroke="var(--coral)" stroke-width="2" stroke-linecap="round" stroke-linejoin="round"><path d="M5 3 L9 3 L10 8 L7.5 9.5 Q9.5 14 14.5 16.5 L16 14 L21 15 L21 19 Q21 21 19 21 Q4 20 3 5 Q3 3 5 3 Z"/><path d="M14 3 Q20 4 21 10"/><path d="M14 7 Q17 7.5 17 10"/></svg>
      (808) 555-0173
    </div>
    <div class="row web">
      <svg viewBox="0 0 24 24" fill="none" stroke="var(--coral)" stroke-width="1.8"><circle cx="12" cy="12" r="9"/><path d="M3 12 H21 M12 3 Q6 12 12 21 M12 3 Q18 12 12 21"/></svg>
      www.PellardCare.example
    </div>
  </div>

  <div class="brand">
    <div class="mark"></div>
    <p class="name">Pellard<br>Homecare</p>
  </div>
</main>
</body>
</html>
```